/ custom plush toys for luxury hotel /

We are, a US company that makes custom plush toys for luxury hotels only. (our customers)
our logo is a mascot:
a teddy bear dressing up as a hotel concierge, the message is: in terms of teddy bear we are your concierge
These plushies are intended to be offered to the children of the customers of these luxurious hotels.
To convince our customers who will land on this site to contact us and work with us, we want to convey the message that our client (the hotel) will make HIS client and HIS children happy by offering them an unexpected gift at the check-in , also to make understand that it is very powerful advertising and marketing object for the hotel (this plush and its LOGO obviously will accompany the children of these customers everywhere).
We also want to insist on the fact that our solution is turnkey, starting from your wishes we take care of everything from the creation of the design to the delivery of the finished products, you do not worry about anything else.
Here is our process:
We only do custom, the customer gives us his theme and ideas and from that we propose different designs, drawing, 3D visualizations, once the design is approved, we make a physical sample that we have validated or modified by our client...
We would like to have a website/landing page to present our concept and our company, also to involve our future customers to contact us by mail or phone, this should be the objective of this page
We want to use themes like teddy bear, luxury, , kids, custom made, handmade, hand drawing..
We really want to emphasize the customization: we create your teddy bear from scratch.
We do not have a catalog because made-to-measure and therefore really want to involve our future customers to contact us by mail.
I can provide you with some of this content (sources file available):
Our Logo
Pictures of some plushies that we made this year
Drawings,
3D
a brief comic strip that we made to present us
Here are some examples attached .
also: Some content that I don't have but that I think would fit in the thematic:
happy children with a teddy bear /
the steps of manufacturing (a seamstress? / the selection of a fabric?) / a designer at work on a drawing board /
etc
Waiting for your proposal,
available if precisions needed
Thank you for your time
Tobi
Luxury Hotel Manager / Purchaser

```html
<!DOCTYPE html>
<html lang="en">
<head>
<meta charset="UTF-8">
<title>PlushPorter – Custom Plush for Luxury Hotels</title>
<link href="https://fonts.googleapis.com/css2?family=Lato:wght@400;700;900&family=Tangerine:wght@700&display=swap" rel="stylesheet">
<style>
:root{
  --orange:#f7a06f;
  --orange-deep:#f3905c;
  --sand:#f6bb78;
  --salmon:#f7967a;
  --gold:#fbbd74;
  --ink:#222;
  --text:#555;
  --dark:#262626;
  --white:#fff;
}
*{margin:0;padding:0;box-sizing:border-box}
html,body{width:1200px;height:3559px;overflow:hidden;background:var(--white)}
body{position:relative;font-family:'Lato',sans-serif;color:var(--ink)}
.abs{position:absolute}
.script{font-family:'Tangerine',cursive;font-weight:700}

/* header */
.logo{left:146px;top:6px;width:128px;height:128px;border-radius:50%;background:var(--white);border:4px solid var(--gold);z-index:5;display:flex;align-items:center;justify-content:center}
.logo-name{left:130px;top:140px;width:160px;text-align:center;font-size:22px;font-weight:900;color:var(--orange);z-index:5}
.logo .badge{width:70px;height:70px;border-radius:50%;background:var(--orange)}
.contact-item{top:10px;display:flex;gap:12px;align-items:flex-start}
.contact-item .label{font-size:12px;font-weight:900;color:var(--ink)}
.contact-item .value{font-size:14px;font-weight:700;color:var(--orange);margin-top:2px}
.contact-item .value.big{font-size:19px}
.nav{top:70px;left:0;width:1200px;height:22px}
.nav a{position:absolute;top:0;font-size:16px;font-weight:700;color:var(--ink);text-decoration:none;letter-spacing:.2px}
.nav a.active{color:var(--orange)}

/* hero */
.hero{left:0;top:110px;width:1200px;height:643px;border-radius:210px 0 210px 0;overflow:hidden;
  background:linear-gradient(100deg,#5e5552 0%,#8b7f78 35%,#cdbfb2 60%,#efe6dc 80%,#e9c1b8 100%)}
.hero h1{left:112px;top:190px;font-size:64px;line-height:52px;color:var(--white);font-family:'Tangerine',cursive;font-weight:700}
.hero p{left:112px;top:322px;width:470px;font-size:15px;line-height:26px;color:var(--white);font-weight:700}
.btn{display:inline-flex;align-items:center;gap:10px;background:var(--orange);color:var(--white);font-size:14px;font-weight:900;text-transform:uppercase;border-radius:22px 0 22px 0;padding:0 24px;height:47px}
.btn .dot{width:13px;height:13px;border-radius:50%;background:var(--white);position:relative}
.btn .dot::after{content:"";position:absolute;left:3px;top:4px;border-left:5px solid var(--orange);border-top:2.5px solid transparent;border-bottom:2.5px solid transparent}
.arrows{display:flex;gap:6px}
.arrows span{width:42px;height:24px;display:flex;align-items:center;justify-content:center;background:var(--white)}
.arrows span.on{background:var(--orange)}

/* about */
.about-frame{left:138px;top:878px;width:425px;height:358px;border:4px solid var(--gold)}
.about-photo{left:112px;top:855px;width:431px;height:360px;background:linear-gradient(135deg,#bfbfbd,#9c9c9a 60%,#b5b5b3)}
.section-title{font-size:44px;color:var(--ink)}
.rule{width:36px;height:3px;background:var(--orange)}
.about-text{left:655px;top:940px;width:415px;font-size:13.5px;line-height:23.2px;color:var(--text);text-align:justify}
.mascot{border-radius:46% 46% 40% 40%;background:radial-gradient(circle at 50% 35%,#a0603a,#6b3a22 60%,#2b2f66 61%,#1f2350)}

/* products */
.products{left:0;top:1335px;width:1200px;height:674px;background:var(--sand);border-radius:150px 0 150px 0}
.center{left:0;width:1200px;text-align:center}
.card{top:1538px;width:234px;height:295px;background:var(--white);padding:9px}
.card .inner{width:100%;height:100%;border:1px solid #e2e2e2;display:flex;flex-direction:column;align-items:center;padding-top:14px}
.card .thumb{width:78px;height:92px;border-radius:40%}
.card h3{margin-top:20px;font-size:14px;font-weight:900;letter-spacing:.2px}
.card .bar{width:28px;height:2px;background:var(--orange);margin-top:10px}
.card p{margin-top:14px;font-size:14px;line-height:20px;color:var(--text);text-align:center}
.mini-dot{margin-top:12px;width:12px;height:12px;border-radius:50%;background:var(--orange);position:relative}
.mini-dot::after{content:"";position:absolute;left:4px;top:3px;border-left:5px solid var(--white);border-top:3px solid transparent;border-bottom:3px solid transparent}

/* process */
.step{top:2185px;width:236px;height:298px;background:var(--white);border-radius:95px 0 95px 0;box-shadow:10px 10px 18px rgba(0,0,0,.08);text-align:center;padding-top:30px}
.step.hot{background:var(--orange)}
.step .icon{width:94px;height:94px;border-radius:50%;background:var(--orange);margin:0 auto;display:flex;align-items:center;justify-content:center}
.step.hot .icon{background:var(--white)}
.step h3{margin-top:24px;font-size:16px;font-weight:700}
.step.hot h3,.step.hot p{color:var(--white)}
.step p{margin:14px auto 0;width:200px;font-size:14px;line-height:22px;color:var(--text)}
.step .more{margin-top:20px;display:inline-flex;gap:6px;align-items:center;font-size:13px;font-weight:700;color:var(--orange)}

/* themes */
.themes{left:0;top:2614px;width:1200px;height:552px;background:var(--salmon)}
.theme{top:2758px;width:324px;height:324px;border-radius:50%;background:var(--gold);box-shadow:0 10px 20px rgba(0,0,0,.08)}
.theme .ring{position:absolute;left:24px;top:24px;width:276px;height:276px;border-radius:50%;background:var(--gold);box-shadow:inset 8px 10px 18px rgba(160,80,20,.35);display:flex;flex-direction:column;align-items:center;justify-content:center}
.theme h3{margin-top:18px;font-size:25px;font-weight:900;color:var(--white)}
.theme .bar{margin-top:18px;width:46px;height:3px;background:var(--white)}

/* footer */
.footer{left:0;top:3166px;width:1200px;height:393px;background:var(--dark);border-top-left-radius:140px}
.fcol h4{font-size:14px;font-weight:900;color:var(--white)}
.fcol .bar{width:24px;height:3px;background:var(--white);margin-top:10px}
.fcol ul{list-style:none;margin-top:20px}
.fcol li{height:34.5px;display:flex;align-items:center;gap:14px;font-size:13px;color:var(--white)}
.fcol li svg,.fcol li .sq{flex:0 0 16px}
.fcol li .sq{width:12px;height:12px;border-radius:50%;background:var(--white)}
.divider{left:112px;top:3490px;width:976px;height:1px;background:#8a8a8a}
.copy{top:3513px;font-size:14px;color:var(--white)}
</style>
</head>
<body>

<!-- header -->
<div class="abs logo"><span class="badge"></span></div>
<div class="abs logo-name">PlushPorter</div>

<div class="abs contact-item" style="left:628px">
  <svg width="30" height="22" viewBox="0 0 30 22" style="margin-top:8px"><rect x="1" y="1" width="28" height="20" fill="none" stroke="#f7a06f" stroke-width="2"/><path d="M1 1 15 12 29 1" fill="none" stroke="#f7a06f" stroke-width="2"/></svg>
  <div><div class="label">EMAIL</div><div class="value">hello@plushporter.com</div></div>
</div>
<div class="abs contact-item" style="left:876px">
  <svg width="30" height="30" viewBox="0 0 30 30" style="margin-top:2px"><circle cx="15" cy="15" r="14" fill="#f7a06f"/><path d="M10 8c1-1 2-1 3 0l1 3-2 2c1 2 3 4 5 5l2-2 3 1c1 1 1 2 0 3-3 3-8 1-11-3s-4-7-1-9z" fill="#fff"/></svg>
  <div><div class="label">CALL US TODAY !</div><div class="value big">+ 1 555 010 2020</div></div>
</div>
<nav class="abs nav">
  <a class="active" style="left:428px">HOME</a>
  <a style="left:519px">ABOUT</a>
  <a style="left:617px">OUR PRODUCTS</a>
  <a style="left:782px">OUR PROCESS</a>
  <a style="left:929px">BLOG</a>
  <a style="left:1015px">CONTACT</a>
</nav>

<!-- hero -->
<section class="abs hero" role="img" aria-label="Photo of a smiling child hugging a cream teddy bear">
  <h1 class="abs">We Create Your Teddy Bear<br>From Scratch</h1>
  <p class="abs">Sed ut perspiciatis unde omnis iste natus error sit voluptatem accusantium doloremque laudantium totam</p>
  <div class="abs" style="left:112px;top:406px;display:flex;gap:16px">
    <span class="btn">Get Started <span class="dot"></span></span>
    <span class="btn">Browse Products <span class="dot"></span></span>
  </div>
  <div class="abs arrows" style="left:112px;top:495px">
    <span><svg width="26" height="10" viewBox="0 0 26 10"><path d="M25 5H2M6 1 2 5l4 4" fill="none" stroke="#222" stroke-width="1.6"/></svg></span>
    <span class="on"><svg width="26" height="10" viewBox="0 0 26 10"><path d="M1 5h23M20 1l4 4-4 4" fill="none" stroke="#fff" stroke-width="1.6"/></svg></span>
  </div>
</section>

<!-- about -->
<div class="abs about-frame"></div>
<div class="abs about-photo" role="img" aria-label="Photo of a white plush turtle embroidered with a hotel logo on a wooden surface"></div>
<h2 class="abs section-title script" style="left:652px;top:860px">About Us</h2>
<div class="abs rule" style="left:655px;top:914px"></div>
<p class="abs about-text">Sed ut perspiciatis unde omnis iste natus error sit voluptatem accusantium doloremque laudantium, totam rem aperiam, eaque ipsa quae ab illo inventore veritatis et quasi architecto beatae vitae dicta sunt explicabo. Nemo enim ipsam voluptatem quia voluptas sit aspernatur aut odit aut fugit, sed quia consequuntur magni dolores eos qui ratione voluptatem sequi nesciunt. Neque porro quisquam est, qui dolorem ipsum quia dolor sit amet, consectetur, adipisci velit, sed quia non numquam eius modi tempora incidunt ut labore et dolore</p>
<span class="abs btn" style="left:655px;top:1171px">Learn More <span class="dot"></span></span>
<div class="abs mascot" style="left:1015px;top:1160px;width:124px;height:194px;z-index:3" role="img" aria-label="Mascot illustration: teddy bear dressed as a hotel concierge, waving"></div>

<!-- products -->
<section class="abs products"></section>
<h2 class="abs center section-title script" style="top:1428px;color:#fff">Our Products</h2>
<div class="abs rule" style="left:582px;top:1484px;background:#fff"></div>

<div class="abs card" style="left:108px"><div class="inner"><div class="thumb" role="img" aria-label="Photo of a black plush bulldog with red scarf" style="background:linear-gradient(#3a3a3a,#222 70%,#c8202a)"></div><h3>PRODUCT TITLE</h3><div class="bar"></div><p>Lorem ipsum dolor sit amet,<br>consectetur adipiscing</p><span class="mini-dot"></span></div></div>
<div class="abs card" style="left:358px"><div class="inner"><div class="thumb" role="img" aria-label="Photo of a tan plush chihuahua with pink bow" style="background:linear-gradient(#e8c7a2,#f1dcc4)"></div><h3>PRODUCT TITLE</h3><div class="bar"></div><p>Lorem ipsum dolor sit amet,<br>consectetur adipiscing</p><span class="mini-dot"></span></div></div>
<div class="abs card" style="left:608px"><div class="inner"><div class="thumb" role="img" aria-label="Photo of a fawn plush pug with pink collar" style="background:linear-gradient(#c9ac8a,#9d8266)"></div><h3>PRODUCT TITLE</h3><div class="bar"></div><p>Lorem ipsum dolor sit amet,<br>consectetur adipiscing</p><span class="mini-dot"></span></div></div>
<div class="abs card" style="left:858px"><div class="inner"><div class="thumb" role="img" aria-label="Photo of a pink plush handbag with a small dog" style="background:linear-gradient(#f2c6d4,#e8a9bf)"></div><h3>PRODUCT TITLE</h3><div class="bar"></div><p>Lorem ipsum dolor sit amet,<br>consectetur adipiscing</p><span class="mini-dot"></span></div></div>

<div class="abs arrows" style="left:555px;top:1877px">
  <span><svg width="26" height="10" viewBox="0 0 26 10"><path d="M25 5H2M6 1 2 5l4 4" fill="none" stroke="#222" stroke-width="1.6"/></svg></span>
  <span class="on"><svg width="26" height="10" viewBox="0 0 26 10"><path d="M1 5h23M20 1l4 4-4 4" fill="none" stroke="#fff" stroke-width="1.6"/></svg></span>
</div>
<div class="abs mascot" style="left:52px;top:1903px;width:162px;height:251px;z-index:3" role="img" aria-label="Mascot illustration: teddy bear concierge in navy uniform, waving"></div>

<!-- process -->
<h2 class="abs center section-title script" style="top:2082px">Our Process</h2>
<div class="abs rule" style="left:582px;top:2137px"></div>

<div class="abs step" style="left:104px">
  <div class="icon"><svg width="44" height="44" viewBox="0 0 44 44"><circle cx="24" cy="9" r="5" fill="#fff"/><rect x="16" y="16" width="16" height="7" rx="2" fill="#fff"/><path d="M4 30h8l8 3h10l10-6v4l-10 7H18l-8-3H4z" fill="#fff"/></svg></div>
  <h3>Getting customer ideas</h3>
  <p>Sed ut perspiciatis unde omn sitvoluptatemaccudoloremque laudantium, totam</p>
  <span class="more">READ MORE <span class="mini-dot" style="margin:0"></span></span>
</div>
<div class="abs step" style="left:356px">
  <div class="icon"><svg width="44" height="44" viewBox="0 0 44 44"><path d="M22 3l2.5 5 5.5.8-4 4 1 5.5-5-2.6-5 2.6 1-5.5-4-4 5.5-.8z" fill="#fff"/><path d="M9 10l1.6 3.2 3.4.5-2.5 2.4.6 3.4-3.1-1.6-3.1 1.6.6-3.4L4 13.7l3.4-.5zM35 10l1.6 3.2 3.4.5-2.5 2.4.6 3.4-3.1-1.6-3.1 1.6.6-3.4-2.5-2.4 3.4-.5z" fill="#fff"/><rect x="10" y="26" width="6" height="14" fill="#fff"/><path d="M18 27l5-6c2-1 3 0 3 2l-1 4h9c2 0 2 3 0 3 2 0 2 3 0 3 2 0 2 3 0 3 1 0 1 3-1 3H18z" fill="#fff"/></svg></div>
  <h3>Working on customer ideas</h3>
  <p>Sed ut perspiciatis unde omn sitvoluptatemaccudoloremque laudantium, totam</p>
  <span class="more">READ MORE <span class="mini-dot" style="margin:0"></span></span>
</div>
<div class="abs step hot" style="left:610px">
  <div class="icon"><svg width="56" height="56" viewBox="0 0 56 56"><path d="M28 3l5 4 6-1 2 6 6 3-1 6 4 5-4 5 1 6-6 3-2 6-6-1-5 4-5-4-6 1-2-6-6-3 1-6-4-5 4-5-1-6 6-3 2-6 6 1z" fill="#f7a06f"/><circle cx="28" cy="28" r="14" fill="none" stroke="#fff" stroke-width="3"/><path d="M21 28l5 5 9-10" fill="none" stroke="#fff" stroke-width="3"/></svg></div>
  <h3>Getting customer approval</h3>
  <p>Sed ut perspiciatis unde omn sitvoluptatemaccudoloremque laudantium, totam</p>
</div>
<div class="abs step" style="left:866px">
  <div class="icon"><svg width="40" height="44" viewBox="0 0 40 44"><circle cx="9" cy="8" r="5" fill="#fff"/><circle cx="31" cy="8" r="5" fill="#fff"/><circle cx="20" cy="15" r="10" fill="#fff"/><ellipse cx="20" cy="32" rx="10" ry="10" fill="#fff"/><circle cx="8" cy="28" r="4" fill="#fff"/><circle cx="32" cy="28" r="4" fill="#fff"/></svg></div>
  <h3>Toy making</h3>
  <p>Sed ut perspiciatis unde omn sitvoluptatemaccudoloremque laudantium, totam</p>
  <span class="more">READ MORE <span class="mini-dot" style="margin:0"></span></span>
</div>

<!-- themes -->
<section class="abs themes"></section>
<h2 class="abs center section-title script" style="top:2670px;color:#fff">Our Themes</h2>
<div class="abs rule" style="left:582px;top:2724px;background:#fff"></div>
<svg class="abs" style="left:50px;top:2906px" width="16" height="26" viewBox="0 0 16 26"><path d="M14 2 3 13l11 11" fill="none" stroke="#fff" stroke-width="3"/></svg>
<svg class="abs" style="left:1134px;top:2906px" width="16" height="26" viewBox="0 0 16 26"><path d="M2 2l11 11L2 24" fill="none" stroke="#fff" stroke-width="3"/></svg>

<div class="abs theme" style="left:111px"><div class="ring">
  <svg width="84" height="84" viewBox="0 0 84 84"><circle cx="22" cy="14" r="8" fill="#fff"/><circle cx="50" cy="14" r="8" fill="#fff"/><circle cx="36" cy="26" r="16" fill="#fff"/><ellipse cx="36" cy="58" rx="18" ry="18" fill="#fff"/><circle cx="16" cy="52" r="6" fill="#fff"/><circle cx="56" cy="52" r="6" fill="#fff"/><rect x="62" y="48" width="14" height="14" fill="#fff"/><rect x="66" y="64" width="14" height="14" fill="#fff"/></svg>
  <h3>Teddy Bear</h3><div class="bar"></div></div></div>
<div class="abs theme" style="left:439px"><div class="ring">
  <svg width="90" height="84" viewBox="0 0 90 84"><path d="M20 6h50l18 22-43 52L2 28z" fill="#fff"/><path d="M2 28h86M20 6l10 22 15 52M70 6 60 28 45 80M30 28 45 6l15 22" fill="none" stroke="#fbbd74" stroke-width="3"/></svg>
  <h3>Luxury</h3><div class="bar"></div></div></div>
<div class="abs theme" style="left:765px"><div class="ring">
  <div role="img" aria-label="Icon of an adult holding a child's hand" style="width:60px;height:84px;border-radius:30px 30px 10px 10px;background:#fff"></div>
  <h3>Kids</h3><div class="bar"></div></div></div>

<!-- footer -->
<footer class="abs footer"></footer>

<div class="abs fcol" style="left:120px;top:3244px">
  <h4>QUICK LINKS</h4><div class="bar"></div>
  <ul>
    <li><svg width="12" height="10" viewBox="0 0 12 10"><path d="M1 1l4 4-4 4M6 1l4 4-4 4" fill="none" stroke="#fff" stroke-width="1.6"/></svg>Home</li>
    <li><svg width="12" height="10" viewBox="0 0 12 10"><path d="M1 1l4 4-4 4M6 1l4 4-4 4" fill="none" stroke="#fff" stroke-width="1.6"/></svg>About</li>
    <li><svg width="12" height="10" viewBox="0 0 12 10"><path d="M1 1l4 4-4 4M6 1l4 4-4 4" fill="none" stroke="#fff" stroke-width="1.6"/></svg>Our Products</li>
    <li><svg width="12" height="10" viewBox="0 0 12 10"><path d="M1 1l4 4-4 4M6 1l4 4-4 4" fill="none" stroke="#fff" stroke-width="1.6"/></svg>Why Choose Us</li>
    <li><svg width="12" height="10" viewBox="0 0 12 10"><path d="M1 1l4 4-4 4M6 1l4 4-4 4" fill="none" stroke="#fff" stroke-width="1.6"/></svg>Reviews</li>
  </ul>
</div>
<div class="abs fcol" style="left:376px;top:3244px">
  <h4>OTHER LINKS</h4><div class="bar"></div>
  <ul>
    <li><svg width="12" height="10" viewBox="0 0 12 10"><path d="M1 1l4 4-4 4M6 1l4 4-4 4" fill="none" stroke="#fff" stroke-width="1.6"/></svg>FAQ</li>
    <li><svg width="12" height="10" viewBox="0 0 12 10"><path d="M1 1l4 4-4 4M6 1l4 4-4 4" fill="none" stroke="#fff" stroke-width="1.6"/></svg>Terms &amp; Conditions</li>
    <li><svg width="12" height="10" viewBox="0 0 12 10"><path d="M1 1l4 4-4 4M6 1l4 4-4 4" fill="none" stroke="#fff" stroke-width="1.6"/></svg>Privacy Policy</li>
    <li><svg width="12" height="10" viewBox="0 0 12 10"><path d="M1 1l4 4-4 4M6 1l4 4-4 4" fill="none" stroke="#fff" stroke-width="1.6"/></svg>Healthy</li>
    <li><svg width="12" height="10" viewBox="0 0 12 10"><path d="M1 1l4 4-4 4M6 1l4 4-4 4" fill="none" stroke="#fff" stroke-width="1.6"/></svg>Contact Us</li>
  </ul>
</div>
<div class="abs fcol" style="left:655px;top:3244px">
  <h4>CONTACT US</h4><div class="bar"></div>
  <ul>
    <li><svg width="12" height="14" viewBox="0 0 12 14"><path d="M6 13S1 7 1 5a5 5 0 0 1 10 0c0 2-5 8-5 8z" fill="#fff"/><circle cx="6" cy="5" r="2" fill="#262626"/></svg>48 Willow Crest Ave.</li>
    <li><span style="width:16px"></span>United States</li>
    <li><svg width="14" height="14" viewBox="0 0 14 14"><path d="M3 1c1-1 2 0 2 0l1 3-1.5 1.5c1 2 2 3 4 4L10 8l3 1s1 1 0 2c-2 2-6 1-9-2S1 3 3 1z" fill="#fff"/></svg>+ 1 555 010 2020</li>
    <li><svg width="14" height="14" viewBox="0 0 14 14"><rect x="3" y="1" width="8" height="4" fill="#fff"/><rect x="1" y="5" width="12" height="8" rx="1" fill="#fff"/><rect x="3" y="8" width="8" height="2" fill="#262626"/></svg>+ 1 555 010 3030</li>
    <li><svg width="14" height="12" viewBox="0 0 14 12"><rect x="1" y="1" width="12" height="10" fill="none" stroke="#fff" stroke-width="1.4"/><path d="M1 1l6 5 6-5" fill="none" stroke="#fff" stroke-width="1.4"/></svg>hello@plushporter.com</li>
  </ul>
</div>
<div class="abs fcol" style="left:967px;top:3244px">
  <h4>FIND US ON</h4><div class="bar"></div>
  <ul>
    <li><span class="sq"></span>Microblog</li>
    <li><span class="sq"></span>Photo Feed</li>
    <li><span class="sq"></span>Community</li>
    <li><span class="sq"></span>Video Channel</li>
  </ul>
</div>

<div class="abs divider"></div>
<div class="abs center copy">Copyrights © 2022 PlushPorter. All Rights Reserved</div>

</body>
</html>
```